FREE Network Assessment image for landing page

This graphic will be on a landing page and on the left will be Text and a download button that we change and control. The graphic for this project will be to the right.
I will add an example of the landing page area so that it makes more sense.

Please include the text from the sample - the font needs to be the same style as what we are using on the left side!

The graphic needs to be a .png file, roughly 713 x 527 white background. Use discretion on design layout.

Colors are black, Red = PMS 1795 and Gray = Cool Gray 10

Thanks,
Tom Harwick

Target Market(s)

small businesses

Industry/Entity Type

Information Technology

Font styles to use
Other font styles liked:
• See sample

Requirements
Must have
• see description
Nice to have
• Possibly small technology related image to help enhance the text but I don't want any image to compete with the text. Keep in mind the colors mentioned in the description - this is the web site colors.
Should not have
• Should not be hard to read

```html
<!DOCTYPE html>
<html lang="en">
<head>
<meta charset="utf-8">
<title>Free Network &amp; Computer Health Check Service</title>
<link rel="stylesheet" href="https://fonts.googleapis.com/css2?family=Jost:wght@400;500;600&display=swap">
<style>
  :root {
    --frame-gray: #5e5a5b;
    --panel-white: #ffffff;
    --ink: #231f20;
    --brand-red: #d9262e;
    --cool-gray: #63666a;
    --art-light: #f4f4f4;
    --art-dark: #8a8a8a;
  }
  html, body {
    margin: 0;
    padding: 0;
    width: 1200px;
    height: 886px;
    overflow: hidden;
    background: var(--frame-gray);
  }
  .canvas {
    position: relative;
    width: 1200px;
    height: 886px;
    background: var(--frame-gray);
  }
  .panel {
    position: absolute;
    left: 41px;
    top: 28px;
    width: 1118px;
    height: 829px;
    background: var(--panel-white);
    overflow: hidden;
  }
  .tech-art {
    position: absolute;
    right: 0;
    top: 0;
    width: 520px;
    height: 100%;
    background:
      radial-gradient(ellipse 70% 60% at 100% 62%, var(--art-dark) 0%, rgba(138,138,138,0.55) 35%, rgba(244,244,244,0) 75%),
      linear-gradient(90deg, rgba(255,255,255,0) 0%, var(--art-light) 55%, #d6d6d6 100%);
  }
  .offer {
    position: absolute;
    left: 45px;
    top: 168px;
    width: 880px;
    font-family: "Jost", "Futura", sans-serif;
    color: var(--ink);
  }
  .offer-title {
    margin: 0 0 16px;
    font-size: 31px;
    font-weight: 600;
    line-height: 1.2;
    letter-spacing: 0.1px;
  }
  .benefits {
    list-style: none;
    margin: 0;
    padding: 0;
  }
  .benefit {
    position: relative;
    padding-left: 69px;
    margin-bottom: 11px;
    font-size: 26.5px;
    font-weight: 400;
    line-height: 37px;
    color: #2e2b2c;
    max-width: 760px;
  }
  .benefit-tick {
    position: absolute;
    left: 20px;
    top: 12px;
    width: 20px;
    height: 18px;
  }
  .cta-button {
    position: absolute;
    left: 45px;
    top: 640px;
    width: 474px;
    height: 79px;
    border-radius: 40px;
    background: var(--brand-red);
    color: #ffffff;
    font-family: "Jost", "Futura", sans-serif;
    font-size: 28.5px;
    font-weight: 500;
    line-height: 79px;
    text-align: center;
    text-decoration: none;
    letter-spacing: -0.2px;
  }
</style>
</head>
<body>
<div class="canvas">
  <div class="panel">
    <div class="tech-art" role="img" aria-label="Abstract grey technology illustration of sweeping curved light streaks and translucent panels"></div>

    <div class="offer">
      <h1 class="offer-title">FREE Network &amp; Computer Health Check Service</h1>
      <ul class="benefits">
        <li class="benefit">
          <svg class="benefit-tick" viewBox="0 0 20 18" aria-hidden="true"><path d="M1 9 L7 16 L19 1" fill="none" stroke="#d9262e" stroke-width="3" stroke-linecap="round" stroke-linejoin="round"/></svg>
          Check your network’s security against hacker attacks, theft, ransomware, viruses, and more.
        </li>
        <li class="benefit">
          <svg class="benefit-tick" viewBox="0 0 20 18" aria-hidden="true"><path d="M1 9 L7 16 L19 1" fill="none" stroke="#d9262e" stroke-width="3" stroke-linecap="round" stroke-linejoin="round"/></svg>
          See who and what has access to your network and data.
        </li>
        <li class="benefit">
          <svg class="benefit-tick" viewBox="0 0 20 18" aria-hidden="true"><path d="M1 9 L7 16 L19 1" fill="none" stroke="#d9262e" stroke-width="3" stroke-linecap="round" stroke-linejoin="round"/></svg>
          Perform network and Internet speed test
        </li>
        <li class="benefit">
          <svg class="benefit-tick" viewBox="0 0 20 18" aria-hidden="true"><path d="M1 9 L7 16 L19 1" fill="none" stroke="#d9262e" stroke-width="3" stroke-linecap="round" stroke-linejoin="round"/></svg>
          Resolve PC slowness issues, security vulnerabilities and improper configurations
        </li>
        <li class="benefit">
          <svg class="benefit-tick" viewBox="0 0 20 18" aria-hidden="true"><path d="M1 9 L7 16 L19 1" fill="none" stroke="#d9262e" stroke-width="3" stroke-linecap="round" stroke-linejoin="round"/></svg>
          Validate your backups are working and recoverable in a timely fashion.
        </li>
      </ul>
    </div>

    <a class="cta-button" href="#">BOOK AN APPOINTMENT NOW!</a>
  </div>
</div>
</body>
</html>
```